Strong, modern, clean Business Card design

Looking for a stunning, but CLEAN business card design. While we are a faith-based organization, we do NOT want this to look religious.

Industry/Entity Type

Non-Profit

Contact Information for Business Card

Dale Munroe | Lead Pastor
dale@BrightHarvestHope.org
970-555-0148
PO Box 7316
Millbrook, NE 80571

Font styles to use
Serif
Sans Serif

Requirements
Should not have
• Religious imagery or symbolism

```html
<!DOCTYPE html>
<html lang="en">
<head>
<meta charset="utf-8">
<title>Bright Harvest Church – Business Card</title>
<link rel="stylesheet" href="https://fonts.googleapis.com/css2?family=Bebas+Neue&family=Josefin+Sans:wght@300;400&display=swap">
<style>
  :root {
    --steel-blue: #4d7a94;
    --band-grey: #b4b4b4;
    --paper: #ffffff;
    --divider: #ffffff;
  }
  html, body {
    margin: 0;
    padding: 0;
    width: 1200px;
    height: 686px;
    overflow: hidden;
    background: var(--paper);
  }
  .card {
    position: relative;
    width: 1200px;
    height: 686px;
    background: var(--paper);
    overflow: hidden;
  }
  .brand {
    position: absolute;
    left: 0;
    top: 150px;
    width: 100%;
    margin: 0;
    text-align: center;
    color: var(--steel-blue);
    font-family: "Josefin Sans", sans-serif;
    font-weight: 400;
  }
  .brand-name {
    display: block;
    font-size: 84px;
    line-height: 1;
    letter-spacing: 6px;
  }
  .brand-sub {
    display: block;
    margin-top: 28px;
    font-size: 52px;
    line-height: 1;
    letter-spacing: 58px;
    padding-left: 58px;
  }
  .title-band {
    position: absolute;
    left: 0;
    top: 427px;
    width: 100%;
    height: 64px;
    background: var(--band-grey);
    box-shadow: 0 6px 10px rgba(0, 0, 0, 0.35);
    z-index: 2;
    display: flex;
    align-items: center;
    justify-content: center;
    font-family: "Bebas Neue", sans-serif;
    color: var(--steel-blue);
    font-size: 56px;
    letter-spacing: 2px;
    line-height: 1;
  }
  .title-band .person { padding-right: 34px; padding-top: 6px; }
  .title-band .role { padding-left: 34px; padding-top: 6px; }
  .title-band .divider {
    width: 3px;
    height: 52px;
    background: var(--divider);
  }
  .contact {
    position: absolute;
    left: 0;
    top: 491px;
    width: 100%;
    height: 195px;
    background: var(--steel-blue);
    z-index: 1;
    color: var(--paper);
    font-family: "Josefin Sans", sans-serif;
    font-weight: 300;
    font-size: 30px;
    line-height: 33.5px;
    text-align: center;
    padding-top: 36px;
    box-sizing: border-box;
    font-style: normal;
  }
  .contact span { display: block; }
</style>
</head>
<body>
  <main class="card">
    <h1 class="brand" aria-label="Bright Harvest Church">
      <span class="brand-name">BRIGHT HARVEST</span>
      <span class="brand-sub">CHURCH</span>
    </h1>

    <div class="title-band">
      <span class="person">DALE MUNROE</span>
      <span class="divider" aria-hidden="true"></span>
      <span class="role">HEAD PASTOR</span>
    </div>

    <address class="contact">
      <span class="email">dale@BrightHarvestHope.org</span>
      <span class="phone">970-555-0148</span>
      <span class="mail">PO Box 7316</span>
      <span class="city">Millbrook, NE 80571</span>
    </address>
  </main>
</body>
</html>
```